Book Cover needed - Disinformation and fake news

I need a book cover (front, back, spine) for the 1st edition of a book entitled ‘Marea Silenciosa’ (Means – Silent Tide) and subtitled ‘Ecos perdidos entre relojes de arena’ (Means - Echoes lost among hourglasses) (inverted commas not to be part of the title and subtitle). The author is ‘Tomás Ferreira’. The finished size of the paperback version will be 5.25" x 8". There will be paperback and e-book versions, so 2 covers will need to be provided: one for the e-book version just with the front cover, and the full book cover for the paperback version.
The final number of pages is expected to be in the region of 350-500 pages. Text for the back cover is down below, and at the bottom of the back cover should have space for the ISBN bar code on the right. The books will be published with RLV - Orvita, so should follow their indications for any specification needed.
The topics discussed include disinformation, fake news, psychological operations. Feel free to design the cover based on those. The design should be original and not include any stock images that have been created by someone else or may require obtaining a copyright license to use.
Back Cover Text (spacing should be respected) :
Ministerio de la verdad, desinformación, “fake news”... en los últimos años nos hemos visto envueltos en una discusión pública rodeados de estos términos sin terminar de entender exactamente qué significan y lo que es peor, sin saber que realmente nos rodean desde que el hombre es hombre.
En esta obra el autor busca acercanos al mundo de la Marea Silenciosa, aquellas operaciones que buscan influir sobre el comportamiento de la población. Sin hacer uso de un lenguaje excesivamente técnico relata como la evolución de la naturaleza de la guerra a los parámetros del siglo XXI promueve un enfoque del conflicto que no supone un uso de la fuerza tradicional. ¿Para qué atacar las instituciones de un país de forma directa, cuando puedes fomentar el conflicto social entre grupos antagónicos y desestabilizar sin realizar un solo disparo?
¿Cómo razona el ser humano? ¿Son nuestras ideas tan nuestras como creemos? ¿Por qué importa tanto el uso preciso del lenguaje a la hora de comunicarnos?, ¿Cómo nos afectan las razones y emociones de los demás? ¿Por qué tendemos a prestar mayor atención a argumentos que encajen con nuestras propias ideas? ¿Cómo nos afecta la conversación en redes sociales?
Armados con el conocimiento que reside en este libro, quizás, seamos menos susceptibles de caer bajo la influencia de grupos con intereses espurios.
General public with an interest on disinformation - fake news

```html
<!DOCTYPE html>
<html lang="es">
<head>
<meta charset="utf-8">
<title>Marea Silenciosa — Tomás Ferreira</title>
<link rel="stylesheet" href="https://fonts.googleapis.com/css2?family=Oswald:wght@500;600;700&family=Open+Sans:ital,wght@1,400&display=swap">
<style>
  :root {
    --page-bg: #ffffff;
    --navy: #0b1a4c;
    --navy-deep: #07123a;
    --title-blue: #1f95ec;
    --title-glow: rgba(40, 150, 255, 0.45);
    --white: #ffffff;
    --art-blue: #2f7fe0;
    --art-cyan: #5ec4ff;
    --art-red: #e0355a;
  }
  * { box-sizing: border-box; margin: 0; padding: 0; }
  html, body {
    width: 1200px; height: 1200px; overflow: hidden;
    background: var(--page-bg);
  }
  .cover-spread {
    position: absolute;
    left: 31px; top: 205px;
    width: 1138px; height: 787px;
    background: var(--navy);
    overflow: hidden;
  }
  /* Back cover */
  .back-cover {
    position: absolute; left: 0; top: 0; width: 516px; height: 100%;
  }
  .back-art-top {
    position: absolute; left: 0; top: 0; width: 230px; height: 170px;
    background: radial-gradient(ellipse at 40% 30%, rgba(90,170,255,0.55), rgba(40,90,200,0.2) 55%, transparent 75%);
  }
  .back-art-bottom {
    position: absolute; left: 0; bottom: 0; width: 516px; height: 200px;
    background:
      radial-gradient(ellipse at 25% 70%, rgba(224,53,90,0.55), transparent 55%),
      radial-gradient(ellipse at 70% 60%, rgba(47,127,224,0.55), transparent 60%),
      linear-gradient(to bottom, transparent, var(--navy-deep));
  }
  .blurb {
    position: absolute; left: 69px; top: 178px; width: 418px;
    font-family: "Open Sans", sans-serif; font-style: italic;
    font-size: 11.2px; line-height: 1.4; color: var(--white);
  }
  .blurb p + p { margin-top: 15px; }
  /* Spine */
  .spine {
    position: absolute; left: 516px; top: 0; width: 112px; height: 100%;
  }
  .spine-text {
    position: absolute; left: 56px;
    font-family: "Oswald", sans-serif; font-weight: 600;
    font-size: 29px; letter-spacing: 1.5px; color: var(--white);
    white-space: nowrap; text-transform: uppercase;
    transform-origin: left center;
    transform: rotate(90deg) translateY(-50%);
    line-height: 1;
  }
  .spine-title { top: 38px; }
  .spine-author { top: 474px; }
  /* Front cover */
  .front-cover {
    position: absolute; left: 628px; top: 0; width: 510px; height: 100%;
    text-align: center;
  }
  .front-title {
    position: absolute; left: 0; right: 0; top: 36px;
    font-family: "Oswald", sans-serif; font-weight: 600;
    font-size: 86px; line-height: 1.03; letter-spacing: 2px;
    color: var(--title-blue); text-transform: uppercase;
    text-shadow: 0 0 18px var(--title-glow);
  }
  .front-subtitle {
    position: absolute; left: 0; right: 0; top: 286px;
    font-family: "Oswald", sans-serif; font-weight: 500;
    font-size: 19px; letter-spacing: 1px; color: var(--white);
    text-transform: uppercase;
  }
  .front-art {
    position: absolute; left: 86px; top: 330px; width: 340px; height: 330px;
  }
  .front-author {
    position: absolute; left: 0; right: 0; top: 698px;
    font-family: "Oswald", sans-serif; font-weight: 600;
    font-size: 36px; letter-spacing: 3px; color: var(--white);
    text-transform: uppercase;
  }
</style>
</head>
<body>
  <main class="cover-spread">
    <section class="back-cover">
      <div class="back-art-top" role="img" aria-label="Faint glowing blue brain illustration"></div>
      <div class="back-art-bottom" role="img" aria-label="Battle scene with silhouetted riders in red and blue smoke"></div>
      <div class="blurb">
        <p>Ministerio de la verdad, desinformación, “fake news”... en los últimos años nos hemos visto envueltos en una discusión pública rodeados de estos términos sin terminar de entender exactamente qué significan y lo que es peor, sin saber que realmente nos rodean desde que el hombre es hombre.</p>
        <p>En esta obra el autor busca acercanos al mundo de la Marea Silenciosa, aquellas operaciones que buscan influir sobre el comportamiento de la población. Sin hacer uso de un lenguaje excesivamente técnico relata como la evolución de la naturaleza de la guerra a los parámetros del siglo XXI promueve un enfoque del conflicto que no supone un uso de la fuerza tradicional. ¿Para qué atacar las instituciones de un país de forma directa, cuando puedes fomentar el conflicto social entre grupos antagónicos y desestabilizar sin realizar un solo disparo?</p>
        <p>¿Cómo razona el ser humano? ¿Son nuestras ideas tan nuestras como creemos? ¿Por qué importa tanto el uso preciso del lenguaje a la hora de comunicarnos?, ¿Cómo nos afectan las razones y emociones de los demás? ¿Por qué tendemos a prestar mayor atención a argumentos que encajen con nuestras propias ideas? ¿Cómo nos afecta la conversación en redes sociales?</p>
        <p>Armados con el conocimiento que reside en este libro, quizás, seamos menos susceptibles de caer bajo la influencia de grupos con intereses espurios.</p>
      </div>
    </section>

    <section class="spine">
      <div class="spine-text spine-title">Marea Silenciosa</div>
      <div class="spine-text spine-author">Tomás Ferreira</div>
    </section>

    <section class="front-cover">
      <h1 class="front-title">Marea<br>Silenciosa</h1>
      <p class="front-subtitle">Ecos perdidos entre relojes de arena</p>
      <svg class="front-art" viewBox="0 0 340 330" role="img" aria-label="Glowing blue brain with a battle scene in red and blue smoke inside">
        <defs>
          <radialGradient id="brain-glow" cx="50%" cy="45%" r="55%">
            <stop offset="0%" stop-color="#5ec4ff"/>
            <stop offset="55%" stop-color="#2f7fe0"/>
            <stop offset="100%" stop-color="#0b1a4c" stop-opacity="0"/>
          </radialGradient>
          <radialGradient id="brain-red" cx="22%" cy="48%" r="30%">
            <stop offset="0%" stop-color="#e0355a" stop-opacity="0.85"/>
            <stop offset="100%" stop-color="#e0355a" stop-opacity="0"/>
          </radialGradient>
        </defs>
        <ellipse cx="170" cy="160" rx="165" ry="160" fill="url(#brain-glow)"/>
        <ellipse cx="170" cy="160" rx="165" ry="160" fill="url(#brain-red)"/>
      </svg>
      <p class="front-author">Tomás Ferreira</p>
    </section>
  </main>
</body>
</html>
```